Wattle Glen Manor Brochure Design

We need a brochure designed for our Aged Care Facility. We need designs that portray warmth and welcoming and at the same time something professional. We have attached the previous brochure and are looking for a modern professional brochure. We are not set on sizing and welcome ideas.

Attachments:
- One more high res photo is available via this link: https://www.filevaultex.net/s/kq52wpx9trmbe3n/Manor_High-Res_18.jpg?dl=0
- Another high res file has been added and is available through this link:
https://www.filevaultex.net/s/mv71cnd8yhsue6r/Manor_High-Res_24.jpg?dl=0

Target Market(s)

Aged Care and families

Requirements
Must have
• Logo and contact details

```html
<!DOCTYPE html>
<html lang="en">
<head>
<meta charset="utf-8">
<title>Wattle Glen Manor – Brochure</title>
<link rel="stylesheet" href="https://fonts.googleapis.com/css2?family=Petit+Formal+Script&family=Bebas+Neue&family=Source+Sans+3:wght@400;600&display=swap">
<style>
  :root {
    --page-bg: #e4e5e7;
    --silver-light: #fbfbfb;
    --silver-mid: #d5d6d8;
    --silver-dark: #a9abae;
    --charcoal: #2b2d30;
    --charcoal-light: #45484c;
    --brand-blue: #0f6d97;
    --brand-blue-deep: #074a6b;
    --brand-blue-bright: #1f93c8;
    --heading-navy: #0b4b6a;
    --ink: #222;
    --white: #fff;
  }
  html, body {
    margin: 0;
    width: 1200px;
    height: 1200px;
    overflow: hidden;
    background: var(--page-bg);
  }
  .brochure {
    position: absolute;
    left: 45px;
    top: 208px;
    width: 1110px;
    height: 784px;
  }
  .script { font-family: "Petit Formal Script", cursive; }
  .heading { font-family: "Bebas Neue", sans-serif; }
  .body-text { font-family: "Source Sans 3", sans-serif; }
</style>
</head>
<body>
<svg class="brochure" viewBox="0 0 1040 735" role="group" aria-label="Wattle Glen Manor tri-fold brochure">
  <defs>
    <linearGradient id="silver" x1="0" y1="0" x2="1" y2="0">
      <stop offset="0" stop-color="var(--silver-dark)"/>
      <stop offset="0.45" stop-color="var(--silver-light)"/>
      <stop offset="0.7" stop-color="var(--silver-mid)"/>
      <stop offset="1" stop-color="var(--silver-dark)"/>
    </linearGradient>
    <linearGradient id="charcoal" x1="0" y1="0" x2="1" y2="1">
      <stop offset="0" stop-color="var(--charcoal-light)"/>
      <stop offset="1" stop-color="var(--charcoal)"/>
    </linearGradient>
    <linearGradient id="blue" x1="0" y1="0" x2="1" y2="1">
      <stop offset="0" stop-color="var(--brand-blue-bright)"/>
      <stop offset="0.5" stop-color="var(--brand-blue)"/>
      <stop offset="1" stop-color="var(--brand-blue-deep)"/>
    </linearGradient>
    <linearGradient id="photo-people" x1="0" y1="0" x2="1" y2="1">
      <stop offset="0" stop-color="#c99a8c"/>
      <stop offset="0.5" stop-color="#e8d6cc"/>
      <stop offset="1" stop-color="#bfc5cc"/>
    </linearGradient>
    <linearGradient id="photo-building" x1="0" y1="0" x2="1" y2="1">
      <stop offset="0" stop-color="#7fb2df"/>
      <stop offset="0.45" stop-color="#9bb387"/>
      <stop offset="1" stop-color="#d8d8d4"/>
    </linearGradient>
  </defs>

  <!-- Panel backgrounds -->
  <rect class="panel-left" x="0" y="0" width="347" height="708" fill="url(#silver)"/>
  <rect class="panel-middle" x="347" y="0" width="346" height="708" fill="url(#charcoal)"/>
  <rect class="panel-right" x="693" y="0" width="347" height="708" fill="url(#silver)"/>

  <!-- Bottom strips -->
  <rect x="0" y="708" width="347" height="27" fill="var(--charcoal)"/>
  <rect x="347" y="708" width="346" height="27" fill="url(#silver)"/>
  <rect x="693" y="708" width="347" height="27" fill="var(--charcoal)"/>

  <!-- Left panel: heading -->
  <g class="script" font-size="21" fill="var(--ink)" text-anchor="middle">
    <text x="173" y="70">Wattle Glen Manor</text>
    <text x="173" y="97">is accredited</text>
    <text x="173" y="124">government funded place</text>
  </g>

  <!-- Left panel: intro box -->
  <path class="intro-box" d="M34 192 Q34 165 62 165 L284 165 Q312 165 312 192 L312 408 L34 490 Z" fill="url(#blue)"/>
  <g class="script" font-size="19" fill="var(--white)" text-anchor="middle">
    <text x="173" y="247">Aged care Facility</text>
    <text x="173" y="279">Offering quality</text>
    <text x="173" y="310">dignity and individuality</text>
    <text x="173" y="341">for residents and their</text>
    <text x="173" y="372">loved ones</text>
  </g>

  <!-- Left panel: photo band -->
  <polygon points="0,505 347,405 347,428 0,520" fill="var(--brand-blue)"/>
  <polygon role="img" aria-label="Photo of a smiling carer and an elderly resident giving thumbs up" points="0,522 347,430 347,708 0,708" fill="url(#photo-people)"/>

  <!-- Middle panel: contact -->
  <g class="contact" text-anchor="middle">
    <text class="heading" x="520" y="102" font-size="30" fill="var(--brand-blue-bright)">CONTACT US TODAY</text>
    <rect x="421" y="106" width="198" height="2" fill="var(--brand-blue-bright)"/>
    <g class="body-text" font-size="17.5" fill="var(--white)">
      <text x="520" y="134">For more information</text>
      <text x="520" y="158">Ph: 07 3555 0142</text>
      <text x="520" y="182">12 Banksia Way</text>
      <text x="520" y="206">(off Wattle Glen Blvd)</text>
      <text x="520" y="229">Glenmara QLD 4079</text>
      <text x="520" y="253">www.wattleglenmanor.com.au</text>
    </g>
  </g>

  <!-- Middle/right: blue framed photo -->
  <polygon points="347,408 895,240 1040,300 1040,312 895,262 347,420" fill="var(--brand-blue)"/>
  <polygon points="347,430 693,600 693,708 347,708" fill="url(#blue)"/>
  <polygon points="693,595 1040,470 1040,708 693,708" fill="url(#silver)"/>
  <polygon points="693,582 1040,462 1040,478 693,598" fill="var(--brand-blue-deep)"/>
  <polygon role="img" aria-label="Photo of the manor building, courtyard and pergolas under a blue sky" points="357,418 895,266 1040,308 1040,462 693,582" fill="url(#photo-building)" stroke="var(--white)" stroke-width="3"/>

  <!-- Middle panel: brand mark -->
  <g class="brand-middle" text-anchor="middle">
    <circle cx="519" cy="608" r="32" fill="#4f7e96"/>
    <text class="heading" x="519" y="670" font-size="22" fill="var(--white)">WATTLE GLEN MANOR</text>
  </g>

  <!-- Right panel: brand mark -->
  <g class="brand-right" text-anchor="middle">
    <circle cx="867" cy="78" r="46" fill="#4f7e96"/>
    <text class="heading" x="867" y="150" font-size="26" fill="var(--charcoal)">WATTLE GLEN MANOR</text>
    <text class="body-text" x="867" y="168" font-size="11" fill="#555" font-style="italic">Quality, Dignity, Individuality</text>
  </g>
  <g class="script" font-size="13" fill="var(--heading-navy)" text-anchor="middle">
    <text x="867" y="200">At Wattle Glen Manor we're commited</text>
    <text x="867" y="218">to your care and comfort</text>
  </g>

  <!-- Right panel: tagline -->
  <g text-anchor="middle">
    <text class="heading" x="867" y="624" font-size="38" fill="var(--charcoal)">PROVIDING AGED CARE</text>
    <text class="heading" x="867" y="660" font-size="38" fill="var(--heading-navy)">WITH QUALITY</text>
    <text class="body-text" x="867" y="686" font-size="18" fill="var(--ink)">www.wattleglenmanor.com.au</text>
  </g>
</svg>
</body>
</html>
```